Pale Lanterns Old Lane Walk Poster Design

We need an A4 sized poster to promote our weekly true crime tours. This poster will be posted onto community noticeboards.
Lots of information and images can be viewed at the following links:-
www.palelanterns.com.au
www.palelanterns.com.au/bookings/
https://www.facebook.com/palelanternsoldlane/
https://www.examplereviews.com.au/Attraction_Review-g000000-d00000000-Reviews-Pale_Lanterns-Newcastle_Greater_Newcastle_New_South_Wales.html
There are also a number of images for possible use at the following link - we are open to intepretation:-
http://palelanterns.com.au/tour-photographs/
The font on our website is "SpecialElite" so we would like to continue using that font type.
Target Market(s)
Adults 25-65.
Font styles to use
Other font styles liked:
- Special Elite
Colors
Designer to choose colors to be used in the design.
Look and feel
Each slider illustrates characteristics of the customer's brand and the style your logo design should communicate.

```html
<!DOCTYPE html>
<html lang="en">
<head>
<meta charset="utf-8">
<title>Pale Lanterns Old Lane Walk – Poster</title>
<link rel="stylesheet" href="https://fonts.googleapis.com/css2?family=Special+Elite&family=Libre+Baskerville:ital@1&family=Ubuntu:wght@400;500&display=swap">
<style>
  :root {
    --backdrop: #d9d9d9;
    --paper: #ffffff;
    --ink: #1c1a18;
    --crime-red: #b3261e;
    --photo-light: #c9c9c9;
    --photo-mid: #8a8a8a;
    --photo-dark: #3a3a3a;
    --wood-light: #ecd3a8;
    --wood-mid: #dcb67e;
    --wood-dark: #c79a5c;
    --band-dark: #3b2f22;
    --band-mid: #6c6256;
    --tear-white: #f7f4ee;
  }
  * { box-sizing: border-box; margin: 0; padding: 0; }
  html, body {
    width: 931px; height: 1200px; overflow: hidden;
    background: var(--backdrop);
  }
  .poster {
    position: absolute; left: 51px; top: 15px;
    width: 828px; height: 1169px;
    background: var(--paper);
    overflow: hidden;
    font-family: "Ubuntu", sans-serif;
    color: var(--ink);
  }
  .tagline {
    position: absolute; top: 28px; left: 0; width: 100%;
    text-align: center;
    font-family: "Libre Baskerville", serif; font-style: italic;
    font-size: 31px; color: var(--crime-red); letter-spacing: 0.5px;
    z-index: 3;
  }
  .street-photo {
    position: absolute; left: 0; top: 40px; width: 828px; height: 470px;
    background:
      linear-gradient(180deg, rgba(255,255,255,0.95) 0%, rgba(255,255,255,0) 22%),
      radial-gradient(ellipse at 30% 60%, var(--photo-dark) 0%, rgba(58,58,58,0) 40%),
      linear-gradient(180deg, var(--photo-light) 0%, var(--photo-mid) 55%, var(--photo-light) 100%);
  }
  .wood-panel {
    position: absolute; left: 0; top: 470px; width: 828px; height: 620px;
    background:
      radial-gradient(ellipse at 85% 8%, rgba(110,70,30,0.55) 0%, rgba(110,70,30,0) 22%),
      linear-gradient(90deg, var(--wood-mid) 0%, var(--wood-light) 40%, var(--wood-light) 65%, var(--wood-dark) 100%);
  }
  .footer-band {
    position: absolute; left: 0; top: 1060px; width: 828px; height: 109px;
    background: linear-gradient(90deg, var(--band-dark) 0%, var(--band-mid) 50%, var(--band-dark) 100%);
  }
  .tear { position: absolute; left: 0; width: 828px; z-index: 2; }
  .tear-top { top: 440px; height: 80px; }
  .tear-bottom { top: 1040px; height: 50px; }

  .brand {
    position: absolute; top: 620px; left: 0; width: 100%;
    display: flex; justify-content: center; align-items: center; gap: 14px;
    z-index: 3;
  }
  .brand-mark { width: 22px; height: 22px; background: var(--ink); }
  .brand-name { font-family: "Ubuntu", sans-serif; font-weight: 500; font-size: 40px; color: var(--ink); letter-spacing: 0.5px; }

  .headline {
    position: absolute; left: 0; width: 100%; text-align: center;
    font-family: "Special Elite", monospace; font-size: 32px; z-index: 3;
  }
  .headline-dark { top: 708px; color: var(--ink); }
  .headline-red { top: 750px; color: var(--crime-red); }

  .highlights {
    position: absolute; top: 813px; left: 56px; width: 740px;
    list-style: disc; font-size: 17px; line-height: 30.5px; color: var(--ink); z-index: 3;
    padding-left: 18px;
  }
  .highlights li::marker { font-size: 12px; }

  .tour-note {
    position: absolute; top: 993px; left: 0; width: 100%; text-align: center;
    font-family: "Special Elite", monospace; font-size: 26px; color: var(--crime-red); z-index: 3;
  }
  .web-address {
    position: absolute; top: 1115px; left: 0; width: 100%; text-align: center;
    font-family: "Ubuntu", sans-serif; font-weight: 500; font-size: 27px;
    letter-spacing: 3.5px; color: #ffffff; z-index: 3;
  }
</style>
</head>
<body>
<main class="poster">
  <p class="tagline">.......stories the city tried to forget.......</p>

  <div class="street-photo" role="img" aria-label="Vintage black and white photograph of a tram on a rainy city street with a figure crossing the road"></div>
  <div class="wood-panel" role="img" aria-label="Light timber wood grain texture"></div>
  <div class="footer-band"></div>

  <svg class="tear tear-top" viewBox="0 0 828 80" preserveAspectRatio="none" aria-hidden="true">
    <path d="M0 52 L40 38 L80 44 L120 30 L170 40 L210 26 L260 34 L300 24 L350 36 L390 30 L430 50 L470 40 L520 56 L560 44 L610 52 L650 40 L700 46 L740 34 L790 42 L828 30 L828 80 L0 80 Z" fill="var(--tear-white)"/>
    <path d="M0 60 L40 48 L80 52 L120 40 L170 48 L210 36 L260 42 L300 34 L350 44 L390 40 L430 58 L470 50 L520 64 L560 54 L610 60 L650 50 L700 54 L740 44 L790 50 L828 40 L828 80 L0 80 Z" fill="var(--wood-mid)"/>
  </svg>

  <svg class="tear tear-bottom" viewBox="0 0 828 50" preserveAspectRatio="none" aria-hidden="true">
    <path d="M0 30 L50 22 L110 28 L170 14 L230 20 L300 10 L360 22 L420 16 L480 26 L540 18 L600 24 L660 16 L720 22 L780 18 L828 24 L828 50 L0 50 Z" fill="var(--tear-white)"/>
    <path d="M0 36 L50 30 L110 34 L170 24 L230 28 L300 20 L360 30 L420 26 L480 32 L540 26 L600 30 L660 24 L720 30 L780 26 L828 32 L828 50 L0 50 Z" fill="var(--band-mid)"/>
  </svg>

  <div class="brand">
    <span class="brand-mark"></span>
    <span class="brand-name">PALE LANTERNS</span>
  </div>

  <h1 class="headline headline-dark">TAKE A WALK ON THE DARK SIDE</h1>
  <h2 class="headline headline-red">REVISIT THE SCENES OF THE CRIMES.</h2>

  <ul class="highlights">
    <li>Retrace the steps of Newcastle's most infamous murderers.</li>
    <li>Descend into the murky world of fraudsters, adulterers and lordly impersonators.</li>
    <li>Unearth the keys to the heart of the Hatchet Lane Killer.</li>
    <li>Relive a time that proves truth is far stranger than fiction.</li>
    <li>Book your ticket for a unique investigation into a dark and crime ridden history.</li>
  </ul>

  <p class="tour-note">weekly true crime tours</p>

  <p class="web-address">WWW.PALELANTERNS.COM.AU</p>
</main>
</body>
</html>
```